Kessler MD Summit Primary Care Business Card

Need a business card for a medical clinic targeting VIP patients. Should portray an upscale feeling. Simple, clean design. Logo and colors need to be incorporated into card. Clinic colors are gray/ silver, blues, white same as logo.
Clinic is a cash only VIP service clinic targeting higher income patients.
Tagline: "Where everyone is a VIP - Very Important Patient"

Target Market(s)

VIP, upscale

Industry/Entity Type

Medical

Contact Information for Business Card

Would like to use for cards with raised print or metallic highlight.

Requirements
Must have
• Incorporate logo, Use colors in logo
Nice to have
• Metallic detail
Should not have
• too much details or colors, other stock photos or designs

```html
<!DOCTYPE html>
<html lang="en">
<head>
<meta charset="utf-8">
<title>Kessler MD Summit Primary Care – Business Card</title>
<link rel="stylesheet" href="https://fonts.googleapis.com/css2?family=Cinzel:wght@500&family=Lora:wght@400&display=swap">
<style>
  :root {
    --backdrop: #3b3b3d;
    --card: #1f1f21;
    --silver: #b9bdc1;
    --silver-dim: #5a5b5e;
    --steel-blue: #3f5369;
    --name-gray: #8e9094;
    --white: #f2f2f2;
  }
  * { margin: 0; padding: 0; box-sizing: border-box; }
  html, body { width: 799px; height: 1200px; overflow: hidden; }
  body {
    background: var(--backdrop);
    position: relative;
    font-family: "Lora", Georgia, serif;
  }
  .card {
    position: absolute;
    left: 80px;
    width: 640px;
    height: 366px;
    background: var(--card);
    overflow: hidden;
  }
  .card--front { top: 150px; }
  .card--back  { top: 690px; }

  .brand {
    position: absolute;
    display: flex;
    align-items: center;
    gap: 12px;
    font-family: "Lora", Georgia, serif;
    font-size: 22px;
    font-weight: 400;
    white-space: nowrap;
  }
  .brand__dot {
    width: 14px; height: 14px; border-radius: 50%;
  }
  .card--front .brand {
    left: 50%; top: 50%;
    transform: translate(-50%, -50%);
    color: var(--silver-dim);
  }
  .card--front .brand__dot { background: var(--silver-dim); }
  .card--back .brand {
    left: 46px; top: 100px;
    color: var(--silver);
  }
  .card--back .brand__dot { background: var(--steel-blue); }

  .identity {
    position: absolute;
    left: 330px; top: 132px;
    color: var(--white);
  }
  .identity__name {
    font-family: "Cinzel", "Times New Roman", serif;
    font-weight: 500;
    font-size: 24px;
    letter-spacing: 1px;
    color: var(--name-gray);
  }
  .identity__title {
    font-size: 13px;
    color: var(--name-gray);
    margin-bottom: 12px;
  }
  .contact { list-style: none; font-size: 16px; line-height: 1.35; }
  .contact__item { display: flex; align-items: center; gap: 10px; }
  .contact__icon { width: 14px; height: 14px; fill: var(--silver); flex: none; }
  .contact__plain { padding-left: 24px; }
  .address { font-size: 16px; line-height: 1.3; margin-top: 2px; }

  .bands { position: absolute; left: 0; bottom: 0; width: 640px; height: 80px; }
  .website {
    position: absolute;
    right: 60px; bottom: 20px;
    font-size: 16px;
    color: var(--white);
  }
</style>
</head>
<body>
  <section class="card card--front" aria-label="Card front">
    <div class="brand"><span class="brand__dot"></span>Kessler Summit</div>
  </section>

  <section class="card card--back" aria-label="Card back">
    <div class="brand"><span class="brand__dot"></span>Kessler Summit</div>

    <div class="identity">
      <h1 class="identity__name">KESSLER SUMMIT</h1>
      <p class="identity__title">Managing Director</p>
      <ul class="contact">
        <li class="contact__item">
          <svg class="contact__icon" viewBox="0 0 16 16" aria-hidden="true"><path d="M3.6 1.5l2.2 2.7-1.3 1.6c.9 2 2.5 3.6 4.5 4.5l1.6-1.3 2.7 2.2-1.4 2.3C6.5 13.2 2.8 9.5 1.3 4.1z"/></svg>
          801-555-0142
        </li>
        <li class="contact__item contact__plain">name@yourwebsite.com</li>
      </ul>
      <p class="address">410 East 200 South<br>Summit Park City 84060</p>
    </div>

    <svg class="bands" viewBox="0 0 640 80" aria-hidden="true">
      <polygon points="0,8 300,8 290,26 0,26" fill="var(--silver)"/>
      <polygon points="300,8 640,8 640,80 260,80" fill="var(--steel-blue)"/>
    </svg>
    <span class="website">www.yourwebsite.com</span>
  </section>
</body>
</html>
```